Vql Centres website for a maxillofacial surgery clinic

It's a website for a clinic for maxillofacial surgery in WordPress . The website doesn't need to be complicated but has to look professional. It needs to be in Dutch so i can give the texts. Similar websites are www.tandartsenpraktijkvoorn.example or www.brekspecialisten.example. Pages would be sort of similar to https://hetcentrumvoorgelaatzorg.example/ or https://veldhovenclinics.example/. Those lasts are maxillofacial surgery clinic websites, but there are little more extensive.
I uploaded the logo. If this is not the proper quality i can upload the eps. Logo was made through artbazaar.

Target Market(s)

Patients who can find me and see information about the clinic

Industry/Entity Type

Healthcare

Coding

Coded - Design and coding required

Number of Pages Required

5+ page

Font styles to use
Other font styles liked:
• Something standard professional

Colors
0054AA
0677BA
7BADD7
CADEEF
E8F1F8

Requirements
Nice to have
• Something in line with the logo. I prefer a little dark like the darker logos but I'm not sure if that's professional. Logos bgtor and wsvp are instances i'm registered to so they will have to be on the website too but small somewhere.

```html
<!DOCTYPE html>
<html lang="nl">
<head>
<meta charset="utf-8">
<title>Vql Centres – Kaakchirurgie</title>
<link href="https://fonts.googleapis.com/css2?family=Open+Sans:wght@400;600;700&family=Nunito+Sans:wght@700;800&family=Tinos:wght@400;700&display=swap" rel="stylesheet">
<style>
:root{
  --navy:#2f4064;
  --navy-deep:#24324f;
  --ink:#3a4a66;
  --blue:#29a3e0;
  --blue-dark:#1f3a8a;
  --lavender:#f2eff8;
  --lav-2:#e6e1f2;
  --muted:#8a8fa0;
  --footer:#262c3b;
  --bar:#2e3d5f;
  --white:#fff;
}
*{box-sizing:border-box;margin:0;padding:0}
html,body{width:1200px;height:4555px;overflow:hidden}
body{position:relative;background:var(--white);font-family:"Open Sans",Arial,sans-serif;color:var(--ink)}
.abs{position:absolute}
.serif{font-family:"Tinos","Times New Roman",serif}
.section{position:absolute;left:0;width:1200px}

/* header */
.header{top:0;height:124px;background:var(--white)}
.top-icon{position:absolute;width:28px;height:28px;border-radius:50%;background:var(--navy);top:18px}
.top-icon svg{position:absolute;left:7px;top:7px}
.top-label{position:absolute;top:18px;font-size:11px;font-weight:600;line-height:14px;color:#222}
.top-label span{display:block;font-weight:400;color:var(--muted);font-size:10px}
.btn-appoint{position:absolute;left:880px;top:12px;width:182px;height:39px;border-radius:20px;background:var(--blue-dark);color:#fff;font-size:11px;font-weight:700;text-align:center;line-height:39px}
.nav a{position:absolute;top:84px;font-size:12px;color:#222;text-decoration:none}
.brand{position:absolute;display:flex;align-items:center;gap:8px;font-family:"Open Sans",Arial,sans-serif;font-weight:600;color:var(--blue)}
.brand i{display:block;border-radius:50%;border:2px solid var(--blue)}

/* hero */
.hero{top:124px;height:770px}
.hero-photo{position:absolute;inset:0;background:linear-gradient(100deg,#2d3d63 0%,#3b5079 45%,#56709a 75%,#344a72 100%)}
.eyebrow{position:absolute;left:88px;color:#fff;font-size:14px;letter-spacing:3px;font-weight:600}
.hero h1{position:absolute;left:88px;font-family:"Nunito Sans",sans-serif;font-weight:800;font-size:44px;line-height:60px;color:#fff}
.hero-rule{position:absolute;left:88px;width:532px;height:1px;background:rgba(255,255,255,.6)}
.hero p{position:absolute;left:90px;width:640px;color:#fff;font-size:15px;line-height:26px;font-weight:600}
.pill{position:absolute;height:38px;border-radius:20px;font-size:13px;font-weight:600;text-align:center;line-height:38px}
.pill.dark{left:83px;width:143px;background:var(--navy);color:#fff}
.pill.light{left:239px;width:180px;background:#fff;color:var(--navy)}

/* about */
.about-photo{position:absolute;left:92px;top:1020px;width:450px;height:450px;border-radius:50%;background:radial-gradient(circle at 45% 45%,#e9c9b4 0%,#b9a39a 35%,#3f6b84 75%,#2e4d66 100%)}
.about-ring{position:absolute;left:80px;top:990px}
.kicker{position:absolute;left:620px;top:1014px;font-size:16px;color:var(--ink)}
.about h2{position:absolute;left:620px;top:1045px;font-size:42px;line-height:54px;font-weight:400;color:var(--ink)}
.quote{position:absolute;left:620px;top:1167px;height:60px;border-left:2px solid var(--navy);padding-left:16px;font-size:13px;line-height:22px;color:var(--muted);width:480px}
.about-body{position:absolute;left:620px;top:1250px;width:470px;font-size:13px;line-height:23px;color:var(--muted)}
.btn-blue{position:absolute;left:619px;top:1400px;width:154px;height:43px;background:var(--blue);color:#fff;font-size:14px;font-weight:700;line-height:43px;padding-left:16px}

/* services */
.services{top:1549px;height:572px;background:var(--lavender)}
.h-center{position:absolute;left:0;width:1200px;text-align:center;font-weight:400;color:var(--ink);font-size:44px}
.sub-center{position:absolute;left:300px;width:600px;text-align:center;font-size:13px;line-height:23px;color:var(--muted)}
.svc-card{position:absolute;top:237px;width:320px;height:268px;border-radius:6px;background:linear-gradient(160deg,#4f6890,#2f4064)}
.svc-card h3{position:absolute;left:20px;top:62px;font-size:26px;color:#fff;font-weight:700}
.svc-icon{position:absolute;top:201px;width:72px;height:72px;border-radius:50%;background:#fff;box-shadow:0 4px 12px rgba(0,0,0,.1)}
.svc-icon svg{position:absolute;left:22px;top:22px}

/* why */
.why-title{top:2170px}
.why-blob{position:absolute;top:2355px;width:380px;height:430px;background:linear-gradient(90deg,rgba(230,225,242,0),var(--lav-2))}
.why-photo{position:absolute;left:399px;top:2360px;width:380px;height:380px;border-radius:50%;background:linear-gradient(180deg,#4b5e8a 0%,#7c8aa8 55%,#5a6577 100%)}
.feat{position:absolute;width:300px}
.feat h4{font-family:"Tinos",serif;font-size:21px;font-weight:400;color:var(--ink);margin-bottom:8px}
.feat p{font-size:12px;line-height:23px;color:var(--muted)}
.feat.left{left:76px;text-align:right}
.feat.right{left:796px}
.feat-icon{position:absolute;width:76px;height:76px;border-radius:50%;background:#fff;box-shadow:0 2px 8px rgba(0,0,0,.08)}
.feat-icon b{position:absolute;left:8px;top:8px;width:60px;height:60px;border-radius:50%;background:var(--navy)}
.feat-icon svg{position:absolute;left:26px;top:26px}

/* hours + form */
.booking{top:2852px;height:560px;background:linear-gradient(90deg,#2d3a58 0%,#3b4d72 50%,#2b3756 100%)}
.hours-title{position:absolute;left:94px;top:130px;font-size:26px;font-weight:400;color:#fff}
.hours{position:absolute;left:96px;top:194px;width:493px;height:237px;background:rgba(30,35,48,.75);border-left:4px solid var(--blue);padding:22px 38px}
.hours-row{display:flex;justify-content:space-between;height:50px;line-height:42px;font-size:14px;color:#fff;border-bottom:1px solid rgba(255,255,255,.25)}
.hours-row:last-child{border:0}
.hours-row b{font-weight:600}
.form-panel{position:absolute;left:612px;top:26px;width:491px;height:499px;background:var(--lavender)}
.form-panel h3{position:absolute;left:100px;top:40px;width:340px;text-align:center;font-size:32px;line-height:42px;font-weight:400;color:var(--ink)}
.form-icon{position:absolute;left:52px;top:52px;width:54px;height:54px;border-radius:50%;background:var(--navy)}
.field{position:absolute;height:50px;background:#fff;border:1px solid #e4e1ec;font-size:13px;color:var(--muted);line-height:50px;padding-left:26px}
.submit{position:absolute;left:54px;top:450px;width:386px;height:51px;background:var(--blue);color:#fff;font-weight:700;font-size:17px;text-align:center;line-height:51px}

/* testimonials */
.reviews{top:3412px;height:700px;background:linear-gradient(180deg,#fff 0%,var(--lavender) 60%,#ebe6f4 100%)}
.rv-card{position:absolute;top:274px;width:322px;height:271px;background:#fff;box-shadow:0 4px 18px rgba(60,60,100,.08);padding:0 28px}
.rv-card.active{border-bottom:5px solid var(--navy)}
.avatar{position:absolute;left:28px;top:-8px;width:62px;height:62px;border-radius:50%;border:4px solid #fff;background:linear-gradient(180deg,#c9b3a4,#6b7d98);box-shadow:0 2px 6px rgba(0,0,0,.15)}
.qmark{position:absolute;right:36px;top:-18px;font-family:"Tinos",serif;font-size:100px;line-height:100px;color:#a9d6f0;font-weight:700}
.rv-card.active .qmark{color:var(--blue)}
.stars{position:absolute;left:28px;top:62px;color:#f39c12;font-size:15px;letter-spacing:3px}
.rv-text{position:absolute;left:28px;top:88px;width:270px;font-size:12px;line-height:23px;color:var(--muted)}
.rv-name{position:absolute;left:28px;top:196px;font-family:"Tinos",serif;font-size:19px;color:var(--navy)}
.rv-role{position:absolute;left:28px;top:222px;font-size:9px;color:#555;letter-spacing:.5px}

/* footer */
.footer{top:4000px;height:555px}
.foot-nav a{position:absolute;top:318px;font-size:13px;font-weight:600;color:#fff;text-decoration:none}
.foot-rule{position:absolute;left:141px;top:369px;width:919px;height:1px;background:rgba(255,255,255,.35)}
.contact{position:absolute;top:412px;display:flex;align-items:center;gap:14px;color:#fff;font-size:11px;font-weight:700;line-height:16px}
.contact .ring{width:56px;height:56px;border-radius:50%;border:1px solid rgba(255,255,255,.7);position:relative;flex:none}
.contact .ring svg{position:absolute;left:16px;top:16px}
.divider{position:absolute;top:405px;width:1px;height:70px;background:rgba(255,255,255,.4)}
.bottom-bar{position:absolute;left:0;top:484px;width:1200px;height:71px;background:var(--bar)}
.bottom-bar .name{position:absolute;left:152px;top:26px;font-size:12px;font-weight:700;color:#fff}
.social{position:absolute;top:22px;width:26px;height:26px;border:1.5px solid #fff;border-radius:3px}
</style>
</head>
<body>

<header class="section header">
  <div class="top-icon" style="left:124px"><svg width="14" height="14" viewBox="0 0 24 24"><path fill="#fff" d="M6.6 10.8a15 15 0 0 0 6.6 6.6l2.2-2.2a1 1 0 0 1 1-.25 11.4 11.4 0 0 0 3.6.57 1 1 0 0 1 1 1V20a1 1 0 0 1-1 1A17 17 0 0 1 3 4a1 1 0 0 1 1-1h3.5a1 1 0 0 1 1 1c0 1.250.2 2.45.57 3.57a1 1 0 0 1-.25 1z"/></svg></div>
  <div class="top-label" style="left:168px">Call Us:<span>(020) 555-0142</span></div>
  <div class="top-icon" style="left:281px"><svg width="14" height="14" viewBox="0 0 24 24"><path fill="#fff" d="M3 5h18v14H3z"/><path fill="none" stroke="#2f4064" stroke-width="2" d="M3 6l9 7 9-7"/></svg></div>
  <div class="top-label" style="left:326px">Email:<span>praktijk@vqlcentres.example</span></div>
  <div class="brand" style="left:532px;top:50px;font-size:20px"><i style="width:18px;height:18px"></i>Vql Centres</div>
  <div class="abs" style="left:707px;top:67px;width:355px;height:1px;background:#ddd"></div>
  <div class="btn-appoint">MAAK EEN AFSPRAAK</div>
  <nav class="nav">
    <a style="left:131px">THUIS</a><a style="left:244px">Behandelingen</a><a style="left:392px">Vergoeding</a>
    <a style="left:712px">Ons team</a><a style="left:841px">Folders</a><a style="left:965px">Contact Us</a>
  </nav>
</header>

<section class="section hero">
  <div class="hero-photo" role="img" aria-label="Foto: kaakchirurg met mondkapje behandelt een glimlachende patiënte"></div>
  <div class="eyebrow" style="top:198px">KAAKCHIRURGIE</div>
  <h1 style="top:234px">Gezichten Kracht Geven,<br>Levens Verbeteren</h1>
  <div class="hero-rule" style="top:368px"></div>
  <p style="top:398px">Lorem ipsum dolor sit amet, consectetur adipiscing elit et dolore conser tempor incididunt ut labore et dolore magna</p>
  <div class="pill dark" style="top:488px">MEER LEREN</div>
  <div class="pill light" style="top:488px">REQUEST QUOTE</div>
  <svg class="abs" style="left:0;top:640px" width="1200" height="132" viewBox="0 0 1200 132">
    <path d="M0 146 L0 24 Q600 240 1200 24 L1200 146 Z" fill="#fff"/>
  </svg>
</section>
<svg class="abs" style="left:0;top:850px" width="1200" height="80" viewBox="0 0 1200 80">
  <path d="M230 8 Q420 32 578 32" fill="none" stroke="var(--blue)" stroke-width="4"/>
  <path d="M622 32 Q780 32 970 8" fill="none" stroke="var(--blue)" stroke-width="4"/>
  <circle cx="600" cy="43" r="23" fill="#fff" stroke="#d7dbe6"/>
  <path d="M591 34c4-3 7 0 9 0s5-3 9 0c3 3 1 10-1 14-1 3-2 8-4 8s-2-6-4-6-2 6-4 6-3-5-4-8c-2-4-4-11-1-14z" fill="none" stroke="var(--blue)" stroke-width="1.5"/>
</svg>

<section class="about">
  <svg class="about-ring" width="480" height="480" viewBox="0 0 480 480"><path d="M30 240 A210 210 0 1 1 240 450" fill="none" stroke="var(--navy)" stroke-width="7" transform="rotate(-10 240 240)"/></svg>
  <div class="about-photo" role="img" aria-label="Foto: lachend jong meisje in de behandelstoel"></div>
  <div class="kicker serif">Geavanceerde Oplossingen</div>
  <h2 class="serif">Innovatie in Maxillofaciale<br>Uitmuntendheid</h2>
  <div class="quote">Lorem ipsum dolor sit amet, consectetur adipiscing elit, sed do eiusmod or incididunt ut labore et dolore</div>
  <div class="about-body">Lorem ipsum dolor sit amet, consectetur adipiscing elit, sed do eiusmod tem por incididunt ut labore et dolore magna aliqua. Ut enim ad minim veniam, quis nostrud exercitation ullamco laboris nisi ut aliquip ex ea commodo consequat. Duis aute irure dolor in reprehenderit in voluptate velit esse cillum dolore eu fugiat nulla pariatur. Excepteur</div>
  <div class="btn-blue">Meer Leren &nbsp;→</div>
</section>

<section class="section services">
  <h2 class="h-center serif" style="top:60px">Onze Diensten</h2>
  <p class="sub-center" style="top:128px">Lorem ipsum dolor sit amet, consectetur adipiscing elit, sed do eiusmod temp or incididunt ut labore et dolore</p>
  <div class="svc-card" style="left:92px" role="img" aria-label="Foto: zorgverleners steken duim omhoog"><h3 class="serif">Kaakchirurgie</h3></div>
  <div class="svc-card" style="left:438px" role="img" aria-label="Foto: lachende patiënte in de stoel"><h3 class="serif">Slaapgeneeskunde</h3></div>
  <div class="svc-card" style="left:786px" role="img" aria-label="Foto: behandelaar met oudere patiënt"><h3 class="serif">Plastische Chirurgie</h3></div>
  <div class="svc-icon" style="left:134px"><svg width="28" height="28" viewBox="0 0 28 28"><g fill="none" stroke="var(--blue)" stroke-width="2"><path d="M4 24V16M10 24V12M16 24v-9M22 24V8"/><circle cx="21" cy="5" r="2.5"/></g></svg></div>
  <div class="svc-icon" style="left:482px"><svg width="28" height="28" viewBox="0 0 28 28"><g fill="none" stroke="var(--blue)" stroke-width="2"><circle cx="14" cy="14" r="11"/><circle cx="14" cy="14" r="6"/><circle cx="14" cy="14" r="2" fill="var(--blue)"/></g></svg></div>
  <div class="svc-icon" style="left:829px"><svg width="28" height="28" viewBox="0 0 28 28"><path d="M11 14V6a3 3 0 0 1 6 0v8l5 2v6a4 4 0 0 1-4 4h-5l-5-6 3-2z" fill="none" stroke="var(--blue)" stroke-width="2"/></svg></div>
</section>

<section class="why">
  <h2 class="h-center serif why-title">Waarom Voor Ons Kiezen</h2>
  <p class="sub-center" style="top:2240px">Lorem ipsum dolor sit amet, consectetur adipiscing elit, sed do eiusmod temp or incididunt ut labore et dolore</p>
  <div class="why-blob" style="left:210px;border-radius:0 220px 220px 0"></div>
  <div class="why-blob" style="left:610px;border-radius:220px 0 0 220px;transform:scaleX(-1)"></div>
  <div class="why-photo" role="img" aria-label="Foto: lachende man in pak met gekruiste armen"></div>

  <div class="feat left" style="top:2398px"><h4>Professioneel</h4><p>Lorem ipsum dolor sit amet, consectet ur adipiscing elit et dolore conser</p></div>
  <div class="feat left" style="top:2529px"><h4>Klantgericht</h4><p>Lorem ipsum dolor sit amet, consectet ur adipiscing elit et dolore conser</p></div>
  <div class="feat left" style="top:2662px"><h4>Persoonlijke Aanpak</h4><p>Lorem ipsum dolor sit amet, consectet ur adipiscing elit et dolore conser</p></div>
  <div class="feat right" style="top:2398px"><h4>Ervaring</h4><p>Lorem ipsum dolor sit amet, consectet ur adipiscing elit et dolore conser</p></div>
  <div class="feat right" style="top:2529px"><h4>Bewezen Track Record</h4><p>Lorem ipsum dolor sit amet, consectet ur adipiscing elit et dolore conser</p></div>
  <div class="feat right" style="top:2662px"><h4>Kwaliteitsborging</h4><p>Lorem ipsum dolor sit amet, consectet ur adipiscing elit et dolore conser</p></div>

  <div class="feat-icon" style="left:402px;top:2402px"><b></b><svg width="24" height="24" viewBox="0 0 24 24"><g fill="none" stroke="#fff" stroke-width="2"><circle cx="12" cy="4" r="2"/><path d="M3 9h18M12 9v5l-5 8M12 14l5 8"/></g></svg></div>
  <div class="feat-icon" style="left:402px;top:2534px"><b></b><svg width="24" height="24" viewBox="0 0 24 24"><g stroke="#fff" stroke-width="2.4" stroke-linecap="round"><path d="M12 2v4M12 18v4M2 12h4M18 12h4M5 5l2.5 2.5M16.5 16.5L19 19M5 19l2.5-2.5M16.5 7.5L19 5"/></g></svg></div>
  <div class="feat-icon" style="left:402px;top:2665px"><b></b><svg width="24" height="24" viewBox="0 0 24 24"><g fill="none" stroke="#fff" stroke-width="2"><path d="M4 12a8 8 0 0 1 16 0"/><path d="M3 13h18v3H3zM8 16v4h8v-4"/></g></svg></div>
  <div class="feat-icon" style="left:696px;top:2402px"><b></b><svg width="24" height="24" viewBox="0 0 24 24"><g fill="none" stroke="#fff" stroke-width="2"><circle cx="12" cy="12" r="10"/><circle cx="12" cy="12" r="5"/><circle cx="12" cy="12" r="1.5" fill="#fff"/></g></svg></div>
  <div class="feat-icon" style="left:696px;top:2534px"><b></b><svg width="24" height="24" viewBox="0 0 24 24"><g fill="none" stroke="#fff" stroke-width="2"><path d="M4 12a8 8 0 0 1 16 0"/><path d="M3 13h18v3H3zM8 16v4h8v-4"/></g></svg></div>
  <div class="feat-icon" style="left:696px;top:2665px"><b></b><svg width="24" height="24" viewBox="0 0 24 24"><g fill="none" stroke="#fff" stroke-width="2"><rect x="2" y="3" width="6" height="6"/><rect x="16" y="15" width="6" height="6"/><rect x="16" y="3" width="6" height="6"/><path d="M8 6h8M19 9v6M5 9v9h11"/></g></svg></div>
</section>

<section class="section booking" role="img" aria-label="Achtergrondfoto: team van de kliniek">
  <h3 class="hours-title serif">Openingstijden</h3>
  <div class="hours">
    <div class="hours-row"><b>Monday - Friday</b><span>08am - 05pm</span></div>
    <div class="hours-row"><b>Saturday</b><span>08am - 05pm</span></div>
    <div class="hours-row"><b>Telephone</b><span>+31 20 555 0198</span></div>
    <div class="hours-row"><b>Email</b><span>info@vqlcentres.example</span></div>
  </div>
  <div class="form-panel">
    <div class="form-icon"><svg class="abs" style="left:15px;top:16px" width="24" height="22" viewBox="0 0 24 22"><g fill="none" stroke="#fff" stroke-width="1.6"><rect x="2" y="6" width="20" height="14"/><path d="M2 7l10 7 10-7M7 2h10v6"/></g></svg></div>
    <h3 class="serif">Aanmelden voor het programma</h3>
    <div class="field" style="left:54px;top:136px;width:184px">First Name</div>
    <div class="field" style="left:256px;top:136px;width:184px">Last Name</div>
    <div class="field" style="left:54px;top:207px;width:184px">Email Address</div>
    <div class="field" style="left:256px;top:207px;width:184px">Phone Number</div>
    <div class="field" style="left:54px;top:281px;width:386px">Select Subject</div>
    <div class="field" style="left:54px;top:352px;width:386px">dd/mm/yyyy</div>
    <div class="submit">SUBMIT</div>
  </div>
</section>

<section class="section reviews">
  <h2 class="h-center serif" style="top:82px">Wat Klanten Zeggen</h2>
  <p class="sub-center" style="top:146px">Lorem ipsum dolor sit amet, consectetur adipiscing elit, sed do eiusmod temp or incididunt ut labore et dolore</p>

  <div class="rv-card" style="left:101px">
    <div class="avatar" role="img" aria-label="Profielfoto klant"></div><div class="qmark">”</div>
    <div class="stars">★★★★★</div>
    <p class="rv-text">Lorem ipsum dolor sit amet, consectetur adipiscing elit, sed do eiusmod tempor inci didunt ut labore et dolore magna aliqua. Ut enim ad minim veniam, quis</p>
    <div class="rv-name">Lotte Verwey</div><div class="rv-role">BUSINESSMAN</div>
  </div>
  <div class="rv-card active" style="left:446px">
    <div class="avatar" role="img" aria-label="Profielfoto klant"></div><div class="qmark">”</div>
    <div class="stars">★★★★★</div>
    <p class="rv-text">Lorem ipsum dolor sit amet, consectetur adipiscing elit, sed do eiusmod tempor inci didunt ut labore et dolore magna aliqua. Ut enim ad minim veniam, quis</p>
    <div class="rv-name">Lotte Verwey</div><div class="rv-role">BUSINESSMAN</div>
  </div>
  <div class="rv-card" style="left:789px">
    <div class="avatar" role="img" aria-label="Profielfoto klant"></div><div class="qmark">”</div>
    <div class="stars">★★★★★</div>
    <p class="rv-text">Lorem ipsum dolor sit amet, consectetur adipiscing elit, sed do eiusmod tempor inci didunt ut labore et dolore magna aliqua. Ut enim ad minim veniam, quis</p>
    <div class="rv-name">Lotte Verwey</div><div class="rv-role">BUSINESSMAN</div>
  </div>
</section>

<footer class="section footer">
  <svg class="abs" style="left:0;top:0" width="1200" height="490" viewBox="0 0 1200 490">
    <path d="M0 30 Q600 170 1200 30 L1200 490 L0 490 Z" fill="var(--footer)"/>
    <path d="M230 78 Q420 102 578 104" fill="none" stroke="var(--blue)" stroke-width="4"/>
    <path d="M622 104 Q780 102 970 78" fill="none" stroke="var(--blue)" stroke-width="4"/>
    <circle cx="600" cy="110" r="23" fill="#fff" stroke="#d7dbe6"/>
    <path d="M591 101c4-3 7 0 9 0s5-3 9 0c3 3 1 10-1 14-1 3-2 8-4 8s-2-6-4-6-2 6-4 6-3-5-4-8c-2-4-4-11-1-14z" fill="none" stroke="var(--blue)" stroke-width="1.5"/>
  </svg>
  <div class="brand" style="left:510px;top:216px;font-size:32px"><i style="width:26px;height:26px"></i>Vql Centres</div>
  <nav class="foot-nav">
    <a style="left:358px">HOME</a><a style="left:450px">SERVICES</a><a style="left:556px">ABOUT US</a><a style="left:676px">TESTIMONIALS</a><a style="left:826px">BLOG</a>
  </nav>
  <div class="foot-rule"></div>
  <div class="contact" style="left:172px">
    <div class="ring"><svg width="24" height="24" viewBox="0 0 24 24"><g fill="none" stroke="#fff" stroke-width="1.5"><circle cx="12" cy="12" r="10"/><path d="M2 12h20M12 2c3 3 3 17 0 20M12 2c-3 3-3 17 0 20"/></g></svg></div>
    <div>Lindelaan 17, Gebouw B<br>1234 AB Veldstad</div>
  </div>
  <div class="divider" style="left:430px"></div>
  <div class="contact" style="left:504px">
    <div class="ring"><svg width="24" height="24" viewBox="0 0 24 24"><g fill="none" stroke="#fff" stroke-width="1.5"><rect x="7" y="2" width="10" height="20" rx="2"/><path d="M11 18h2"/></g></svg></div>
    <div>PHONE<br><span style="font-weight:400">(020) 555-0198</span></div>
  </div>
  <div class="divider" style="left:750px"></div>
  <div class="contact" style="left:827px">
    <div class="ring"><svg width="24" height="24" viewBox="0 0 24 24"><g fill="none" stroke="#fff" stroke-width="1.5"><rect x="2" y="5" width="20" height="14"/><path d="M2 6l10 7 10-7"/></g></svg></div>
    <div>EMAIL<br><span style="font-weight:400">info@vqlcentres.example</span></div>
  </div>
  <div class="bottom-bar">
    <div class="name">Vql Centres</div>
    <div class="social" style="left:933px"></div>
    <div class="social" style="left:966px"></div>
    <div class="social" style="left:999px"></div>
    <div class="social" style="left:1032px"></div>
  </div>
</footer>

</body>
</html>
```